Business Card Design Mabel Style

I make Hand Made Name necklaces which are known as Mabel Style and would like a Shiny Gold Business Card almost to look like a Gold Bar.
on the 2nd side I want an image of a Mabel Necklace in Silver as it will be on a Gold Background.

Industry/Entity Type

Business

Contact Information for Business Card

Trovane Jewellery UK
Lettered Chains Direct

Neil Fothergill
Director
M: 07700 900 312

www.trovgems.co.uk

Requirements
Must have
• Writing must be in Black

Card must be metallic gold

```html
<!DOCTYPE html>
<html lang="en">
<head>
<meta charset="utf-8">
<title>Trovane Jewellery UK – Business Card</title>
<link rel="stylesheet" href="https://fonts.googleapis.com/css2?family=Questrial&display=swap">
<style>
  :root {
    --page-bg: #ffffff;
    --ink: #111111;
    --gold-deep: #b86f06;
    --gold-mid: #e39a1c;
    --gold-light: #f7c25a;
    --gold-shine: #ffd98a;
    --night: #140d07;
    --night-warm: #3a2510;
    --sparkle: #8a5a1c;
    --silver-light: #f4f4f4;
    --silver-mid: #cfcfcf;
    --silver-dark: #9a9a9a;
  }
  * { margin: 0; padding: 0; box-sizing: border-box; }
  html, body {
    width: 1200px;
    height: 900px;
    overflow: hidden;
    background: var(--page-bg);
  }
  .canvas {
    width: 1200px;
    height: 900px;
    display: flex;
    align-items: center;
    justify-content: center;
    gap: 60px;
  }
  .card {
    position: relative;
    width: 520px;
    height: 300px;
    border-radius: 24px;
    overflow: hidden;
  }

  /* Front: brushed gold bar */
  .card--front {
    background:
      repeating-linear-gradient(180deg, rgba(255,255,255,0.07) 0 2px, rgba(0,0,0,0.05) 2px 5px, rgba(255,255,255,0) 5px 9px),
      linear-gradient(180deg, var(--gold-light) 0%, var(--gold-mid) 35%, var(--gold-shine) 62%, var(--gold-mid) 80%, var(--gold-deep) 100%);
    font-family: "Questrial", sans-serif;
    color: var(--ink);
  }
  .brand {
    position: absolute;
    top: 30px;
    left: 26px;
    display: flex;
    align-items: flex-start;
    gap: 12px;
  }
  .brand__dot {
    flex: none;
    width: 44px;
    height: 44px;
    border-radius: 50%;
    border: 3px solid var(--ink);
    margin-top: 2px;
  }
  .brand__name {
    font-size: 24px;
    line-height: 1;
    letter-spacing: -0.3px;
  }
  .brand__tagline {
    margin-top: 5px;
    font-size: 13px;
    white-space: nowrap;
  }
  .watermark {
    position: absolute;
    left: 110px;
    top: 125px;
    width: 380px;
    height: 150px;
    border-radius: 60px;
    background: radial-gradient(ellipse at center, rgba(150, 80, 0, 0.18), rgba(150, 80, 0, 0) 70%);
  }
  .person {
    position: absolute;
    left: 26px;
    top: 180px;
  }
  .person__name { font-size: 17px; }
  .person__role { font-size: 10px; margin-top: 2px; }
  .contact {
    position: absolute;
    left: 24px;
    bottom: 30px;
    list-style: none;
    font-size: 16px;
  }
  .contact__item {
    display: flex;
    align-items: center;
    gap: 8px;
    line-height: 22px;
    white-space: nowrap;
  }
  .contact__icon { width: 14px; height: 14px; flex: none; }

  /* Back: dark sparkle ground with necklace image area */
  .card--back {
    background:
      linear-gradient(90deg, rgba(138,90,28,0.4), rgba(138,90,28,0) 30%, rgba(138,90,28,0) 70%, rgba(138,90,28,0.4)),
      radial-gradient(ellipse at 50% 55%, var(--night-warm) 0%, var(--night) 65%);
  }
  .necklace-image {
    position: absolute;
    left: 40px;
    top: 95px;
    width: 400px;
    height: 140px;
    border-radius: 70px 50px 60px 40px;
    background:
      radial-gradient(ellipse at 40% 35%, var(--silver-light) 0%, var(--silver-mid) 55%, var(--silver-dark) 100%);
  }
  .necklace-chain {
    position: absolute;
    inset: 0;
    width: 100%;
    height: 100%;
  }
</style>
</head>
<body>
  <main class="canvas">
    <section class="card card--front" aria-label="Business card front">
      <div class="brand">
        <span class="brand__dot" aria-hidden="true"></span>
        <div>
          <p class="brand__name">Trovane<br>Jewellery</p>
          <p class="brand__tagline">UK Lettered Chains Direct</p>
        </div>
      </div>
      <div class="watermark" role="img" aria-label="Faint Mabel Style name lettering in the gold"></div>
      <div class="person">
        <p class="person__name">Neil Fothergill</p>
        <p class="person__role">Director</p>
      </div>
      <ul class="contact">
        <li class="contact__item">
          <svg class="contact__icon" viewBox="0 0 24 24" aria-hidden="true"><path fill="#111" d="M6.6 10.8a15.2 15.2 0 0 0 6.6 6.6l2.2-2.2a1 1 0 0 1 1-.25 11.4 11.4 0 0 0 3.6.57 1 1 0 0 1 1 1V20a1 1 0 0 1-1 1A17 17 0 0 1 3 4a1 1 0 0 1 1-1h3.5a1 1 0 0 1 1 1c0 1.25.2 2.45.57 3.57a1 1 0 0 1-.25 1z"/></svg>
          07700 900 312
        </li>
        <li class="contact__item">
          <svg class="contact__icon" viewBox="0 0 24 24" aria-hidden="true"><g fill="none" stroke="#111" stroke-width="2"><circle cx="12" cy="12" r="10"/><ellipse cx="12" cy="12" rx="4" ry="10"/><path d="M2 12h20M4 7h16M4 17h16"/></g></svg>
          www.trovgems.co.uk
        </li>
      </ul>
    </section>

    <section class="card card--back" aria-label="Business card back">
      <svg class="necklace-chain" viewBox="0 0 520 300" aria-hidden="true">
        <g fill="none" stroke="#bdbdbd" stroke-width="2">
          <path d="M20 0 C30 40 38 80 52 120"/>
          <path d="M520 110 C500 140 470 165 440 180"/>
        </g>
      </svg>
      <div class="necklace-image" role="img" aria-label="Silver Mabel Style name necklace"></div>
    </section>
  </main>
</body>
</html>
```